Professional & Modern Technology Business Card

We need a business card for our software/technology firm. Our services include Program/Project Management, Project Controls and Enterprise Analytics. Our clients are usually in the Aviation, Public Works, Transportation and Electric & Water Utility industries. We serve both public and private clients. Would like a very professional, conservative but somewhat modern design. Design, Develop, Deploy is the corporate tagline. We have two offices. The headquarters is in Atlanta, GA and a satellite office In Savannah, GA. Corporate Logo Attached.
Looking to do website and corporate brochure after the successful completion of this project. Would like to begin a working relationship with best designers.
Tagline: Design, Develop, Deploy
Website: www.quelvanesystems.example
My Name: Marla Dunstead
My Title: CEO
Email: mdunstead@quelvanesystems.example
Atlanta Address:
87 Corliss Avenue, #2291
Atlanta, GA 30301
Office: 404.555.0182
Fax: 404.555.0147
Mobile: 404.555.0163
Savannah Address:
350 West Harrow Bend Road
Suite 720
Savannah, GA 31401
Office: 912.555.0139
Fax: 404.555.0147
Mobile: 404.555.0163
Updates
Please include the email address in your designs: mdunstead@quelvanesystems.example.
I appreciate everyone's design efforts. Just a few notes:
1. Please remove the mobile number from the cards
2. The backs of the cards can be utilized for writing notes. Make sure your design on the back of the card is conducive to clearly adding writing if needed.
3. No black backgrounds please
4. Only use the corporate logo on the front of the card. You can use portions of the logo design, but not the logo in totality.
Thank You
Industry/Entity Type
Conservative
Look and feel
Each slider illustrates characteristics of the customer's brand and the style your logo design should communicate.

```html
<!DOCTYPE html>
<html lang="en">
<head>
<meta charset="utf-8">
<title>Quelvane Systems, Inc. — Business Card</title>
<link rel="stylesheet" href="https://fonts.googleapis.com/css2?family=Open+Sans:ital,wght@0,400;0,600;0,700;1,400&display=swap">
<style>
  :root {
    --backdrop: #3b3b3b;
    --card-front: #f4f4f1;
    --card-back: #ffffff;
    --ink: #231f20;
    --brand-blue: #1b8fd2;
    --brand-yellow: #e6c300;
    --brand-green: #8dc63f;
  }
  * { margin: 0; padding: 0; box-sizing: border-box; }
  html, body { width: 1200px; height: 900px; overflow: hidden; }
  body {
    background: var(--backdrop);
    font-family: "Open Sans", Arial, sans-serif;
    position: relative;
  }
  .card {
    position: absolute;
    top: 301px;
    width: 514px;
    height: 296px;
    overflow: hidden;
    color: var(--ink);
  }
  .card--front { left: 72px; background: var(--card-front); }
  .card--back { left: 615px; background: var(--card-back); }

  .front-glow {
    position: absolute;
    right: 0; top: 0;
    width: 260px; height: 296px;
    background: radial-gradient(ellipse at 70% 45%, rgba(230,195,0,0.18), rgba(27,143,210,0.08) 45%, transparent 75%);
  }
  .wordmark {
    position: absolute;
    display: flex;
    align-items: center;
    gap: 12px;
    font-weight: 700;
    letter-spacing: -0.5px;
    line-height: 1.05;
    color: var(--ink);
  }
  .wordmark__dot {
    width: 34px; height: 34px;
    border-radius: 50%;
    background: var(--brand-yellow);
    flex: none;
  }
  .card--front .wordmark { left: 40px; top: 112px; font-size: 27px; }
  .card--back .wordmark { left: 34px; top: 42px; font-size: 22px; }
  .card--back .wordmark__dot { width: 28px; height: 28px; }

  .tagline {
    position: absolute;
    left: 86px; top: 262px;
    font-size: 11px;
    font-style: italic;
    letter-spacing: 6.5px;
  }

  .person { position: absolute; left: 331px; top: 76px; }
  .person__name { color: var(--brand-blue); font-size: 18px; font-weight: 400; line-height: 1.2; }
  .person__title { font-size: 12px; margin-top: 2px; }

  .office {
    position: absolute;
    top: 172px;
    font-size: 12px;
    line-height: 16.5px;
  }
  .office--satellite { left: 61px; }
  .office--main { left: 331px; }
  .office__label { font-weight: 600; }
  .office__row { display: flex; }
  .office__key { width: 47px; }
  .office--main .office__key { color: var(--brand-blue); width: 45px; }

  .contact-band {
    position: absolute;
    left: 0; bottom: 0;
    width: 100%; height: 28px;
    background: var(--brand-yellow);
    display: flex;
    justify-content: center;
    gap: 14px;
    font-size: 12px;
    line-height: 28px;
  }
</style>
</head>
<body>
  <section class="card card--front" aria-label="Card front">
    <div class="front-glow"></div>
    <div class="wordmark"><span class="wordmark__dot"></span><span>Quelvane<br>Systems, Inc.</span></div>
    <p class="tagline">DESIGN, DEVELOP, DEPLOY</p>
  </section>

  <section class="card card--back" aria-label="Card back">
    <div class="wordmark"><span class="wordmark__dot"></span><span>Quelvane<br>Systems, Inc.</span></div>

    <div class="person">
      <p class="person__name">Marla Dunstead</p>
      <p class="person__title">CEO</p>
    </div>

    <div class="office office--satellite">
      <p class="office__label">Satellite Office:</p>
      <p>350 West Harrow Bend Road, Suite 720</p>
      <p>Savannah, GA 31401</p>
      <p class="office__row"><span class="office__key">Office:</span>912.555.0139</p>
      <p class="office__row"><span class="office__key">Fax:</span>404.555.0147</p>
    </div>

    <div class="office office--main">
      <p class="office__label">Main Office:</p>
      <p>87 Corliss Avenue, #2291</p>
      <p>Atlanta, GA 30301</p>
      <p class="office__row"><span class="office__key">Office:</span>404.555.0182</p>
      <p class="office__row"><span class="office__key">Fax:</span>404.555.0147</p>
    </div>

    <p class="contact-band"><span>www.quelvanesystems.example</span><span>|</span><span>mdunstead@quelvanesystems.example</span></p>
  </section>
</body>
</html>
```